Print on top the name of the company: (Or Similar)
Larkmoor Cleaning & Disinfecting
Because your standards aren't standard.

We adhere to ALL NVB guidelines for both residential and commercial cleaning.

Infection Control is our ultimate goal.

Instructions:
Opening a residential and commercial cleaning and disinfecting company in south Florida.

Targeting high-end residential clients, commercial and healthcare facilities, specializing in Ambulatory Care Guidelines. With a concentration and expertise in targeting Covid 19 and other transmissible pathogens.

UMRE trained.
Owned and operated by a licensed BSN Registered Nurse specially ​trained in Infection Control Prevention with over 25 years experience. Over two decades in Ambulatory Surgery Center Administration, Director of Nursing and Infection Control Prevention ad Consulting.

Looking to create a business flier that emphasizes Cleaning & Disinfection
along with the standard expectation for residential and Commercial cleaning services
Updates

Need extra days to review

Target Market(s)

Residential & Commercial

Font styles to use
Decorative

Requirements
Must have
• A checklist for cleaning services

```html
<!DOCTYPE html>
<html lang="en">
<head>
<meta charset="utf-8">
<title>Larkmoor Cleaning &amp; Disinfecting</title>
<link rel="stylesheet" href="https://fonts.googleapis.com/css2?family=Open+Sans:wght@800&family=Arimo:ital,wght@0,400;1,700&family=Didact+Gothic&display=swap">
<style>
  :root {
    --green: #559100;
    --yellow: #fbe03f;
    --white: #ffffff;
    --ink: #5a3a0a;
    --phone: #3b1f0e;
    --photo-warm: #d9642a;
    --photo-cool: #3aa8d8;
    --photo-dark: #2a2430;
  }
  * { margin: 0; padding: 0; box-sizing: border-box; }
  html, body { width: 927px; height: 1200px; overflow: hidden; background: var(--white); }
  .flyer { position: relative; width: 927px; height: 1200px; overflow: hidden; background: var(--yellow); }
  .hero-photo {
    position: absolute; left: 0; top: 0; width: 927px; height: 516px;
    background:
      radial-gradient(ellipse at 15% 25%, rgba(255,170,60,.9), transparent 45%),
      radial-gradient(ellipse at 60% 55%, var(--photo-cool), transparent 50%),
      linear-gradient(160deg, var(--photo-warm) 0%, #7a3a40 40%, var(--photo-dark) 100%);
  }
  .green-panel { position: absolute; left: 0; top: 0; width: 927px; height: 1200px; }
  .headline {
    position: absolute; left: 0; top: 78px; width: 927px; text-align: center;
    font-family: "Open Sans", sans-serif; font-weight: 800; color: var(--white);
    font-size: 68px; line-height: 82px; letter-spacing: 0.5px;
    text-shadow: 0 2px 6px rgba(0,0,0,.35);
  }
  .tagline {
    position: absolute; left: 0; top: 248px; width: 927px; text-align: center;
    font-family: "Arimo", sans-serif; font-style: italic; font-weight: 700;
    font-size: 24px; color: var(--white); text-shadow: 0 1px 4px rgba(0,0,0,.4);
  }
  .supplies-illustration {
    position: absolute; left: 494px; top: 378px; width: 390px; height: 353px;
    border-radius: 30px;
    background: radial-gradient(ellipse at 50% 55%, #2aa7a0 0%, #7fd14a 45%, rgba(251,224,63,0) 75%);
  }
  .service-group { position: absolute; left: 70px; font-family: "Didact Gothic", sans-serif; color: var(--white); }
  .service-group h2 { font-weight: 400; font-size: 27px; letter-spacing: .6px; margin-bottom: 14px; }
  .service-group li { list-style: none; font-size: 21px; letter-spacing: .9px; }
  .commercial { top: 522px; }
  .commercial li { line-height: 25px; }
  .residential { top: 795px; }
  .residential li { line-height: 26px; }
  .checklist {
    position: absolute; left: 489px; top: 775px; width: 372px;
    font-family: "Didact Gothic", sans-serif; color: var(--ink);
    font-size: 20px; line-height: 24px; letter-spacing: .5px;
  }
  .checklist li { list-style: none; position: relative; padding-left: 26px; margin-bottom: 8px; }
  .checklist li::before { content: "\2713"; position: absolute; left: 0; top: 0; font-weight: 700; }
  .call-badge { position: absolute; left: 334px; top: 1014px; width: 154px; height: 154px; }
  .phone {
    position: absolute; left: 510px; top: 1052px;
    font-family: "Arimo", sans-serif; font-size: 62px; line-height: 70px;
    color: var(--phone); letter-spacing: -1.5px; white-space: nowrap;
  }
</style>
</head>
<body>
<main class="flyer">
  <div class="hero-photo" role="img" aria-label="Photo of a blue-gloved hand wiping a dark table with a microfiber cloth, spray bottle blurred behind"></div>

  <svg class="green-panel" viewBox="0 0 927 1200" aria-hidden="true">
    <polygon points="0,396 463,516 349,1200 0,1200" fill="var(--green)"/>
  </svg>

  <h1 class="headline">LARKMOOR CLEANING<br>&amp; DISINFECTING</h1>
  <p class="tagline">Because your standards aren't standard.</p>

  <div class="supplies-illustration" role="img" aria-label="Illustration of a teal bucket filled with cleaning sprays, bottles, brushes, gloves and a squeegee"></div>

  <section class="service-group commercial">
    <h2>COMMERCIAL</h2>
    <ul>
      <li>Janitorial</li>
      <li>Offices</li>
      <li>Floor maintenance</li>
      <li>Carpet cleaning</li>
      <li>Move-ins</li>
      <li>Construction clean-ups</li>
      <li>Estate clean-outs</li>
    </ul>
  </section>

  <section class="service-group residential">
    <h2>RESIDENTIAL</h2>
    <ul>
      <li>House cleaning</li>
      <li>Before &amp; after party</li>
      <li>Move-ins</li>
      <li>Move-outs</li>
      <li>Holiday cleaning</li>
      <li>Seasonal cleaning</li>
      <li>Carpet Cleaning</li>
      <li>Deodorizing &amp; sanitizing</li>
    </ul>
  </section>

  <ul class="checklist">
    <li>We adhere to ALL NVB guidelines for both residential and commercial cleaning.</li>
    <li>Infection Control is our ultimate goal.</li>
    <li>UMRE trained.</li>
    <li>Owned and operated by a licensed BSN Registered Nurse specially trained in Infection Control Prevention with over 25 years experience.</li>
  </ul>

  <svg class="call-badge" viewBox="0 0 154 154" role="img" aria-label="Call now">
    <defs>
      <radialGradient id="badgeFill" cx="40%" cy="35%" r="70%">
        <stop offset="0" stop-color="#b7f04a"/>
        <stop offset="0.6" stop-color="#5fbf12"/>
        <stop offset="1" stop-color="#3a8a05"/>
      </radialGradient>
    </defs>
    <circle cx="77" cy="77" r="75" fill="url(#badgeFill)"/>
    <g transform="rotate(-18 77 77)" font-family="Open Sans, sans-serif" font-weight="800" fill="#ffffff" text-anchor="middle">
      <text x="77" y="72" font-size="34">CALL</text>
      <text x="77" y="106" font-size="34">NOW</text>
    </g>
  </svg>

  <p class="phone">555-218-4907</p>
</main>
</body>
</html>
```